Feature Nomination Banner

Create a 600 x 160 banner advertisement for Counsel Ledger Quarterly’s feature story nominations. We’ve included the Counsel Ledger Quarterly logo (black and white versions) for inclusion.
Headline: Now Accepting Nominations for 2024 Features
Nominate an Outstanding Lawyer or Law Firm Today!

```html
<!DOCTYPE html>
<html lang="en">
<head>
<meta charset="utf-8">
<title>Feature Nomination Banner – Versions</title>
<link rel="stylesheet" href="https://fonts.googleapis.com/css2?family=Archivo:wght@400;600;700;800&display=swap">
<style>
  :root {
    --page: #ffffff;
    --ink: #463a28;
    --brand-ink: #111111;
    --gold: #b59a5e;
    --banner-light: #f8f8f8;
    --banner-mid: #ececec;
    --banner-edge: #e0e0e0;
    --shadow: #3e301c;
    --photo-tone: rgba(150, 108, 70, 0.22);
    --photo-tone-soft: rgba(200, 170, 140, 0.18);
  }
  * { box-sizing: border-box; margin: 0; padding: 0; }
  html, body {
    width: 1200px; height: 1200px; overflow: hidden;
    background: var(--page);
  }
  body {
    position: relative;
    font-family: "Archivo", "Helvetica Neue", Arial, sans-serif;
    color: var(--ink);
  }
  .version-label {
    position: absolute; left: 0; width: 1200px;
    text-align: center;
    font-weight: 700; font-size: 24px; line-height: 28px;
    letter-spacing: 0.36em; text-indent: 0.36em;
    color: var(--ink);
  }
  .banner-shadow {
    position: absolute; left: 22px; width: 1155px; height: 30px;
    background: var(--shadow);
    filter: blur(7px);
    border-radius: 0 0 50% 50% / 0 0 70% 70%;
  }
  .banner {
    position: absolute; left: 3px; width: 1195px; height: 319px;
    overflow: hidden;
    background: radial-gradient(ellipse at 35% 40%, var(--banner-light) 0%, var(--banner-mid) 70%, var(--banner-edge) 100%);
  }
  .photo {
    position: absolute; top: 0; height: 319px; width: 420px;
    background: linear-gradient(90deg,
      transparent 0%, var(--photo-tone-soft) 20%,
      var(--photo-tone) 50%, var(--photo-tone-soft) 80%, transparent 100%);
  }
  .brand-name {
    position: absolute;
    font-weight: 600; font-size: 19px; line-height: 24px;
    letter-spacing: 0.02em;
    color: var(--brand-ink); text-transform: uppercase; white-space: nowrap;
  }
  .headline {
    position: absolute;
    font-weight: 800; font-size: 42px; line-height: 45px;
    text-transform: uppercase;
    color: var(--ink); white-space: nowrap;
  }
  .subline {
    position: absolute;
    font-weight: 400; font-size: 26px; line-height: 30px;
    color: var(--gold); white-space: nowrap;
  }
  .is-left .brand-name { left: 54px; top: 258px; }
  .is-left .headline  { left: 47px; top: 333px; }
  .is-left .subline   { left: 47px; top: 436px; }
  .is-centered .brand-name, .is-centered .headline, .is-centered .subline {
    left: 0; width: 824px; text-align: center;
  }
  .is-centered .brand-name { top: 762px; }
  .is-centered .headline  { top: 837px; }
  .is-centered .subline   { top: 939px; }
</style>
</head>
<body>
  <div class="version-label" style="top:138px;">VERSION 1</div>
  <div class="banner-shadow" style="top:500px;"></div>
  <section class="banner" style="top:192px;">
    <div class="photo" role="img" aria-label="Photo of a bronze Lady Justice statue with a gavel and stacked law books" style="left:720px;"></div>
  </section>
  <div class="is-left">
    <div class="brand-name">Counsel Ledger Quarterly</div>
    <h1 class="headline">Now Accepting Nominations<br>for 2024 Features</h1>
    <p class="subline">Nominate an Outstanding Lawyer or Law Firm Today!</p>
  </div>

  <div class="version-label" style="top:648px;">VERSION 2</div>
  <div class="banner-shadow" style="top:1010px;"></div>
  <section class="banner" style="top:702px;">
    <div class="photo" role="img" aria-label="Photo of a bronze Lady Justice statue with a gavel and stacked law books" style="left:770px;"></div>
  </section>
  <div class="is-centered">
    <div class="brand-name">Counsel Ledger Quarterly</div>
    <h2 class="headline">Now Accepting Nominations<br>for 2024 Features</h2>
    <p class="subline">Nominate an Outstanding Lawyer or Law Firm Today!</p>
  </div>
</body>
</html>
```